Design the World's Greatest Valentine's Day Greeting Card

We're looking for designers who can create the best Valentine's Day greeting card designs in the world. Your design could be could be extra special because it is funny, beautiful, inspiring or original.

Your designs should be able to fit on a standard 4"x6" greeting card. The main design will need to be for the front page (cover) of the card, but you can also include some design for the inside pages if you like.

Multiple winners will be awarded, and will be chosen within 5 days after the contest ends on February 13, 2019.
First Prize: $200
Runners-up: $100 each

The winning card design (or designs) could be recognised as standout designs publicly, as they can be used, by Gigmarten.com, at it sole discretion, in some Gigmarten.com marketing or PR materials.

Let's celebrate Valentine's Day together by showcasing your designs!

```html
<!DOCTYPE html>
<html lang="en">
<head>
<meta charset="utf-8">
<title>Happy Valentine's Day Card</title>
<link rel="stylesheet" href="https://fonts.googleapis.com/css2?family=Fredericka+the+Great&display=swap">
<style>
  :root {
    --paper: #ffffff;
    --ink: #111111;
    --frame: #000000;
    --heart: #ff0d0d;
    --heart-edge: #ffffff;
    --bf-pink: #ff3fa8;
    --bf-blue: #2f3cf0;
    --bf-cyan: #2fd6f0;
    --bf-lime: #8ef02f;
    --bf-orange: #ff9a2a;
    --bf-yellow: #f7f03a;
    --bf-violet: #9a2ff0;
  }
  html, body {
    margin: 0;
    padding: 0;
    width: 800px;
    height: 1200px;
    overflow: hidden;
    background: var(--paper);
  }
  .card {
    position: relative;
    width: 800px;
    height: 1200px;
    background: var(--paper);
    overflow: hidden;
    font-family: "Fredericka the Great", "Georgia", serif;
  }
  .butterfly-band {
    position: absolute;
    opacity: 0.55;
    background: linear-gradient(90deg, var(--bf-orange), var(--bf-blue), var(--bf-pink), var(--bf-lime), var(--bf-cyan), var(--bf-violet), var(--bf-orange), var(--bf-pink));
  }
  .butterfly-band--top { left: 0; top: 0; width: 800px; height: 60px; }
  .butterfly-band--bottom { left: 0; top: 1164px; width: 800px; height: 36px; }
  .butterfly-band--left { left: 0; top: 160px; width: 25px; height: 1000px;
    background: linear-gradient(180deg, var(--bf-pink), var(--bf-cyan), var(--bf-violet), var(--bf-orange), var(--bf-lime), var(--bf-blue)); opacity: 0.4; }

  .frame-bar { position: absolute; background: var(--frame); }
  .frame-bar--top { left: 25px; top: 60px; width: 764px; height: 27px; }
  .frame-bar--left { left: 25px; top: 60px; width: 27px; height: 1076px; }
  .frame-bar--right { left: 760px; top: 129px; width: 27px; height: 991px; }
  .frame-bar--bottom { left: 83px; top: 1095px; width: 704px; height: 25px; }

  .inner-panel {
    position: absolute;
    left: 52px; top: 87px;
    width: 708px; height: 1049px;
    background: var(--paper);
  }
  .butterfly-field {
    position: absolute;
    left: 83px; top: 133px;
    width: 677px; height: 962px;
    opacity: 0.5;
    background:
      radial-gradient(circle at 20% 15%, var(--bf-pink) 0, transparent 22%),
      radial-gradient(circle at 80% 20%, var(--bf-blue) 0, transparent 24%),
      radial-gradient(circle at 15% 55%, var(--bf-lime) 0, transparent 22%),
      radial-gradient(circle at 75% 60%, var(--bf-cyan) 0, transparent 26%),
      radial-gradient(circle at 40% 85%, var(--bf-orange) 0, transparent 22%),
      radial-gradient(circle at 85% 88%, var(--bf-violet) 0, transparent 22%),
      radial-gradient(circle at 50% 35%, var(--bf-yellow) 0, transparent 20%),
      var(--paper);
  }

  .word-box {
    position: absolute;
    background: var(--paper);
    display: flex;
    align-items: center;
    justify-content: center;
    color: var(--ink);
    line-height: 1;
    white-space: nowrap;
  }
  .word-box--happy { left: 213px; top: 240px; width: 365px; height: 124px; font-size: 108px; }
  .word-box--valentines { left: 84px; top: 524px; width: 649px; height: 134px; font-size: 100px; }
  .word-box--day { left: 307px; top: 844px; width: 200px; height: 125px; font-size: 108px; }

  .hearts {
    position: absolute;
    left: 0; top: 0;
    width: 800px; height: 1200px;
  }
  .heart { fill: var(--heart); stroke: var(--heart-edge); stroke-width: 4; }
</style>
</head>
<body>
  <main class="card">
    <div class="butterfly-band butterfly-band--top" role="img" aria-label="Band of colourful butterflies"></div>
    <div class="butterfly-band butterfly-band--left" role="img" aria-label="Colourful butterflies along the edge"></div>
    <div class="butterfly-band butterfly-band--bottom" role="img" aria-label="Band of colourful butterflies"></div>

    <div class="inner-panel"></div>
    <div class="butterfly-field" role="img" aria-label="Scattered rainbow butterflies forming swirling heart shapes"></div>

    <div class="frame-bar frame-bar--top"></div>
    <div class="frame-bar frame-bar--left"></div>
    <div class="frame-bar frame-bar--right"></div>
    <div class="frame-bar frame-bar--bottom"></div>

    <h1 class="word-box word-box--happy">Happy</h1>
    <div class="word-box word-box--valentines">Valentine’s</div>
    <div class="word-box word-box--day">Day</div>

    <svg class="hearts" viewBox="0 0 800 1200" aria-hidden="true">
      <defs>
        <path id="heart-shape" d="M50 92 C22 66 0 46 0 26 C0 10 12 0 27 0 C39 0 46 8 50 18 C54 8 61 0 73 0 C88 0 100 10 100 26 C100 46 78 66 50 92Z"/>
      </defs>
      <use href="#heart-shape" class="heart" transform="translate(158 60) scale(0.98)"/>
      <use href="#heart-shape" class="heart" transform="translate(211 128) scale(0.98)"/>
      <use href="#heart-shape" class="heart" transform="translate(650 410) scale(0.98)"/>
      <use href="#heart-shape" class="heart" transform="translate(610 473) scale(0.98)"/>
      <use href="#heart-shape" class="heart" transform="translate(275 715) scale(0.98)"/>
      <use href="#heart-shape" class="heart" transform="translate(216 778) scale(0.98)"/>
    </svg>
  </main>
</body>
</html>
```